Harbor Ridge Chapel
Every Man, Woman, and Child
Modern
Mark Fenwick
lead Pastor
4527 Delford
Marlow Bay, Ca 90417
mark.fenwick@harborridgechapel.example
harborridgechapel.example
front of the card is the logo, and all the info on the back
use the logo, and try harbor ridge chapel behind the logo and try it under the logo.

```html
<!DOCTYPE html>
<html lang="en">
<head>
<meta charset="utf-8">
<title>Harbor Ridge Chapel – Business Card</title>
<link rel="stylesheet" href="https://fonts.googleapis.com/css2?family=Source+Sans+3:wght@400;600;700&display=swap">
<style>
  :root {
    --backdrop: #e9e6e1;
    --card-black: #232323;
    --brand-blue: #2b78b6;
    --rule-grey: #8a8a8a;
    --text-white: #ffffff;
    --text-grey: #d2d2d2;
  }
  * { box-sizing: border-box; margin: 0; padding: 0; }
  html, body {
    width: 1200px; height: 780px; overflow: hidden;
    background: var(--backdrop);
    font-family: "Source Sans 3", "Helvetica Neue", Arial, sans-serif;
  }
  .canvas {
    width: 1200px; height: 780px;
    display: flex; align-items: center; justify-content: center;
  }
  .business-card {
    position: relative;
    width: 1040px; height: 620px;
    background: var(--card-black);
    border-radius: 38px;
    overflow: hidden;
    color: var(--text-white);
  }
  .brand-lockup {
    position: absolute; top: 62px; left: 0; right: 0;
    display: flex; flex-direction: column; align-items: center;
  }
  .brand-mark {
    width: 120px; height: 120px; border-radius: 50%;
    background: var(--brand-blue);
  }
  .brand-name {
    margin-top: 26px;
    font-size: 50px; font-weight: 400; letter-spacing: 1px;
    text-transform: uppercase; color: var(--text-white);
  }
  .name-band {
    position: absolute; left: 0; right: 0; top: 338px; height: 66px;
    background: var(--brand-blue);
    display: flex; align-items: center; justify-content: center;
    font-size: 30px;
  }
  .name-band::before, .name-band::after {
    content: ""; position: absolute; left: 0; right: 0; height: 3px;
    background: var(--rule-grey);
  }
  .name-band::before { top: -9px; }
  .name-band::after { bottom: -9px; }
  .person-name { font-weight: 700; }
  .person-role { font-weight: 400; margin-left: 8px; }
  .street-address {
    position: absolute; top: 440px; left: 0; right: 0;
    text-align: center; font-size: 24px; color: var(--text-grey);
  }
  .contact-row {
    position: absolute; left: 52px; right: 44px; bottom: 62px;
    display: flex; justify-content: space-between; align-items: center;
    font-size: 22px; color: var(--text-grey);
  }
  .contact-item { display: flex; align-items: center; gap: 8px; white-space: nowrap; }
  .contact-icon { width: 22px; height: 22px; flex: none; }
</style>
</head>
<body>
<main class="canvas">
  <article class="business-card">
    <header class="brand-lockup">
      <span class="brand-mark" aria-hidden="true"></span>
      <h1 class="brand-name">Harbor Ridge Chapel</h1>
    </header>

    <div class="name-band">
      <span class="person-name">Mark Fenwick</span>
      <span class="person-role">/ lead Pastor</span>
    </div>

    <p class="street-address">4527 Delford, Marlow Bay, Ca 90417</p>

    <footer class="contact-row">
      <span class="contact-item">
        <svg class="contact-icon" viewBox="0 0 24 24" aria-hidden="true">
          <path fill="#2b78b6" d="M6.6 10.8a15.2 15.2 0 0 0 6.6 6.6l2.2-2.2a1 1 0 0 1 1-.25 11.4 11.4 0 0 0 3.6.57 1 1 0 0 1 1 1V20a1 1 0 0 1-1 1A17 17 0 0 1 3 4a1 1 0 0 1 1-1h3.5a1 1 0 0 1 1 1c0 1.25.2 2.45.57 3.6a1 1 0 0 1-.25 1z"/>
        </svg>
        949 555-0142
      </span>
      <span class="contact-item">
        <svg class="contact-icon" viewBox="0 0 24 24" aria-hidden="true">
          <rect x="2" y="5" width="20" height="14" rx="2" fill="#2b78b6"/>
          <path d="M3 6.5l9 6.5 9-6.5" fill="none" stroke="#232323" stroke-width="1.6"/>
        </svg>
        mark.fenwick@harborridgechapel.example
      </span>
      <span class="contact-item">
        <svg class="contact-icon" viewBox="0 0 24 24" aria-hidden="true">
          <circle cx="12" cy="12" r="10" fill="#2b78b6"/>
          <path d="M2 12h20M12 2c3 3 3 17 0 20M12 2c-3 3-3 17 0 20" fill="none" stroke="#232323" stroke-width="1.3"/>
        </svg>
        harborridgechapel.example
      </span>
    </footer>
  </article>
</main>
</body>
</html>
```